Gutscheine
Zielgruppe
Immobilienmakler, Verkauf und Vermietung, Immobilienbewertung
Aufgabenstellung
Es soll eine Gutscheinkarte werden für die Verteilung auf einen Stadtfest am Stand vor unserem Büro.
Es soll ein Bezug zu Immobilien haben, aber auch eine Emotion vermitteln. Daher Bild mit Familie oder Rentner. Zielgruppe sollen sein zum einen junge Leute, die vor haben eine Immobilie zu kaufen. Und auf der anderen Seite Leute, die mit dem Gedanken spielen eine Immobilie aus Altersgründen, Trennung, Scheidung oder nach Erbe zu verkaufen. Dominant soll mit dem Gutschein zur kostenlosen Bewertung einer Immobilie gelockt werden.
Auf der Rückseite soll es so sein, dass Kunden ankreuzen können, ob Sie eine Immobilie evtl. Verkaufen möchten und eine kostenlose Bewertung wünschen.
Evtl. macht es Sinn zwei Karten anzulegen. Einmal Zielgruppe Käufer/Suchende, einmal Verkäufer.
Beim Format bin ich flexibel und für alles . Es kann länglich sein, aber auch quadratisch.
Vom Design einen Bezug zu den bisherigen Flyern und Broschüren im Anhang.
Bilder die auf der Homepage sind, sind als Stockbilder vorhanden.
Es werden noch einige andere Sachen für das Stadtfest benötigt. Wie Bierdeckel, Imagebroschüre zum Aufklappen, Banner, Roll-Up, Luftballons.

```html
<!DOCTYPE html>
<html lang="de">
<head>
<meta charset="utf-8">
<title>Gutscheinkarten Marbach Immobilien</title>
<link rel="stylesheet" href="https://fonts.googleapis.com/css2?family=Libre+Caslon+Display&family=Open+Sans:wght@400;500&display=swap">
<style>
  :root {
    --stage: #5a5a5a;
    --navy: #243a66;
    --gold: #bfa14f;
    --white: #ffffff;
    --ink: #2a2f3f;
  }
  * { box-sizing: border-box; margin: 0; padding: 0; }
  html, body { width: 1200px; height: 598px; overflow: hidden; background: var(--stage); }
  .sheet { position: relative; width: 1200px; height: 598px; }
  .card { position: absolute; width: 545px; height: 257px; background: var(--white); overflow: hidden; font-family: "Open Sans", sans-serif; }
  .card--front-seller { left: 25px; top: 25px; }
  .card--front-buyer { left: 630px; top: 25px; }
  .card--back-seller { left: 25px; top: 314px; }
  .card--back-buyer { left: 630px; top: 314px; }

  /* Front */
  .photo { position: absolute; left: 0; top: 0; width: 355px; height: 257px; }
  .photo--interior { background: linear-gradient(160deg, #f1f1ef 0%, #e6e4df 45%, #d9d4cb 75%, #ece9e3 100%); }
  .photo--house { background: linear-gradient(180deg, #b9a493 0%, #e8b56a 35%, #f4d9a4 52%, #e6ece0 70%, #cfdcb8 100%); }
  .frame-line { position: absolute; left: 25px; top: 25px; height: 103px; border-left: 1.5px solid; border-top: 1.5px solid; }
  .frame-line--light { width: 330px; border-color: rgba(255,255,255,.95); }
  .frame-line--navy { width: 432px; border-color: var(--navy); }
  .title-panel { position: absolute; left: 0; top: 175px; width: 255px; height: 82px; background: rgba(255,255,255,.72); border-top: 2.5px solid var(--gold); }
  .title-bar { position: absolute; left: 255px; top: 175px; width: 8px; height: 82px; background: var(--navy); }
  .voucher-title { position: absolute; left: 24px; top: 185px; font-family: "Libre Caslon Display", serif; font-size: 49px; line-height: 1; color: var(--navy); letter-spacing: .5px; }
  .brand-mark { position: absolute; right: 27px; top: 27px; display: flex; align-items: center; gap: 8px; }
  .brand-mark__name { font-size: 9px; letter-spacing: 1.5px; color: var(--navy); text-transform: uppercase; }
  .brand-mark__square { width: 37px; height: 37px; background: var(--gold); }
  .accent-line { position: absolute; left: 518px; top: 87px; width: 1.5px; height: 48px; }
  .accent-line--gold { background: var(--gold); }
  .accent-line--navy { background: var(--navy); }
  .offer { position: absolute; right: 25px; top: 156px; text-align: right; font-size: 14.5px; line-height: 20.5px; color: var(--navy); letter-spacing: .4px; }

  /* Back */
  .backdrop { position: absolute; inset: 0; background: linear-gradient(120deg, #fbfaf8 0%, #f4f1ec 45%, #ede6dc 70%, #e9ddcd 100%); }
  .back-heading { position: absolute; left: 50px; top: 50px; font-family: "Libre Caslon Display", serif; font-size: 23px; color: var(--navy); }
  .choice { position: absolute; left: 50px; display: flex; align-items: center; font-size: 11.3px; color: var(--ink); letter-spacing: .4px; }
  .choice__box { width: 11px; height: 11px; border: 1.3px solid var(--ink); margin-right: 19px; flex: none; }
  .phone-line { position: absolute; left: 51px; top: 196px; font-size: 11.3px; color: var(--ink); letter-spacing: .4px; }
  .footer-strip { position: absolute; left: 0; top: 230px; width: 289px; height: 27px; background: var(--white); }
  .footer-bar { position: absolute; left: 289px; top: 230px; width: 8px; height: 27px; background: var(--navy); }
  .brand-block { position: absolute; left: 430px; top: 26px; width: 90px; text-align: center; }
  .brand-block__square { width: 54px; height: 54px; margin: 0 auto 10px; background: var(--gold); }
  .brand-block__name { font-family: "Libre Caslon Display", serif; font-size: 18px; letter-spacing: 1.5px; color: var(--navy); line-height: 1; }
  .brand-block__sub { font-size: 5.5px; letter-spacing: 1.5px; color: var(--navy); margin-top: 3px; }
  .contact { position: absolute; left: 427px; top: 178px; font-size: 7.7px; line-height: 11px; color: var(--ink); letter-spacing: .3px; }
  .contact__row { display: flex; gap: 5px; }
  .contact__row svg { flex: none; margin-top: 1px; }
  .contact__row + .contact__row { margin-top: 4px; }
</style>
</head>
<body>
<div class="sheet">

  <section class="card card--front-seller">
    <div class="photo photo--interior" role="img" aria-label="Helles, modernes Wohninterieur mit Treppe und Galerie"></div>
    <div class="frame-line frame-line--light"></div>
    <div class="title-panel"></div>
    <div class="title-bar"></div>
    <h1 class="voucher-title">Gutschein</h1>
    <div class="brand-mark"><span class="brand-mark__name">Marbach</span><span class="brand-mark__square"></span></div>
    <div class="accent-line accent-line--gold"></div>
    <p class="offer">Kostenlose<br>Wertermittlung<br>&amp; Verkaufsberatung<br>für Eigentümer</p>
  </section>

  <section class="card card--front-buyer">
    <div class="photo photo--house" role="img" aria-label="Modernes weißes Einfamilienhaus im Sonnenuntergang"></div>
    <div class="frame-line frame-line--navy"></div>
    <div class="title-panel"></div>
    <div class="title-bar"></div>
    <h1 class="voucher-title">Gutschein</h1>
    <div class="brand-mark"><span class="brand-mark__name">Marbach</span><span class="brand-mark__square"></span></div>
    <div class="accent-line accent-line--navy"></div>
    <p class="offer">Kostenlose<br>Immobilienbewertung<br>&amp; Beratung für<br>Kaufinteressenten</p>
  </section>

  <section class="card card--back-seller">
    <div class="backdrop" role="img" aria-label="Blasses Wohnzimmer mit Sofa und Treppe im Hintergrund"></div>
    <h2 class="back-heading">Bitte ankreuzen</h2>
    <div class="choice" style="top:100px"><span class="choice__box"></span>Ich möchte den realen Wert meiner Immobilie erfahren</div>
    <div class="choice" style="top:139px;align-items:flex-start"><span class="choice__box"></span><span style="margin-top:8px">Ich erwäge einen Verkauf</span></div>
    <p class="phone-line">Telefon: ___________________________________________</p>
    <div class="brand-block">
      <div class="brand-block__square"></div>
      <div class="brand-block__name">MARBACH</div>
      <div class="brand-block__sub">IMMOBILIEN</div>
    </div>
    <div class="contact">
      <div class="contact__row"><svg width="9" height="9" viewBox="0 0 24 24" fill="none" stroke="#2a2f3f" stroke-width="2"><path d="M5 3h4l2 5-3 2a12 12 0 0 0 6 6l2-3 5 2v4a2 2 0 0 1-2 2A18 18 0 0 1 3 5a2 2 0 0 1 2-2z"/></svg><span>02241 55 20 317</span></div>
      <div class="contact__row"><svg width="9" height="10" viewBox="0 0 24 24" fill="none" stroke="#2a2f3f" stroke-width="2"><path d="M12 22s7-7 7-12a7 7 0 0 0-14 0c0 5 7 12 7 12z"/><circle cx="12" cy="10" r="2.5"/></svg><span>Marbach Immobilien<br>Lindenallee 12<br>53721 Siegburg<br>Deutschland</span></div>
    </div>
    <div class="footer-strip"></div>
    <div class="footer-bar"></div>
  </section>

  <section class="card card--back-buyer">
    <div class="backdrop" role="img" aria-label="Blasses Wohnzimmer mit Sofa und Treppe im Hintergrund"></div>
    <h2 class="back-heading">Bitte ankreuzen</h2>
    <div class="choice" style="top:98px"><span class="choice__box" style="margin-right:22px"></span>Ich suche eine Immobilie zum Kauf</div>
    <div class="choice" style="top:144px"><span class="choice__box" style="margin-right:22px"></span>Ich möchte eine kostenlose Immobilienbewertung</div>
    <p class="phone-line" style="left:28px;top:193px">Telefon: ___________________________________________</p>
    <div class="brand-block">
      <div class="brand-block__square"></div>
      <div class="brand-block__name">MARBACH</div>
      <div class="brand-block__sub">IMMOBILIEN</div>
    </div>
    <div class="contact">
      <div class="contact__row"><svg width="9" height="9" viewBox="0 0 24 24" fill="none" stroke="#2a2f3f" stroke-width="2"><path d="M5 3h4l2 5-3 2a12 12 0 0 0 6 6l2-3 5 2v4a2 2 0 0 1-2 2A18 18 0 0 1 3 5a2 2 0 0 1 2-2z"/></svg><span>02241 55 20 317</span></div>
      <div class="contact__row"><svg width="9" height="10" viewBox="0 0 24 24" fill="none" stroke="#2a2f3f" stroke-width="2"><path d="M12 22s7-7 7-12a7 7 0 0 0-14 0c0 5 7 12 7 12z"/><circle cx="12" cy="10" r="2.5"/></svg><span>Marbach Immobilien<br>Lindenallee 12<br>53721 Siegburg<br>Deutschland</span></div>
    </div>
    <div class="footer-strip"></div>
    <div class="footer-bar"></div>
  </section>

</div>
</body>
</html>
```